Mend ORX Syndrome (Non-Profit) Tri-Fold Brochure Design

We have put together the content for a brochure that we will distribute to doctors, researchers and patients about our non-profit. We would like the design of the brochure to look more professional and have nice aesthetics. It needs to incorporate all of the content in the attached Word file. We will have printed once we have a finished design.

Target Market(s)

Medical

Industry/Entity Type

Non Profit

Font styles to use
Serif
Sans Serif

Colors
33a6d7

Requirements
Must have
• Must include all content provided. Professional.
Nice to have
• Colors

```html
<!DOCTYPE html>
<html lang="en">
<head>
<meta charset="utf-8">
<title>Mend ORX Syndrome – Tri-Fold Brochure</title>
<link rel="stylesheet" href="https://fonts.googleapis.com/css2?family=Poppins:wght@300;400;600;700;800;900&family=Roboto:wght@400;500;700&display=swap">
<style>
:root{
  --bg:#8a8a8a;
  --teal:#2fc0cc;
  --teal-light:#3cc7d2;
  --blue:#33a6d7;
  --blue-deep:#1d8fd0;
  --navy:#0f3c66;
  --ink:#333;
  --paper:#ffffff;
  --paper-grey:#f0f1f3;
  --white:#fff;
}
*{margin:0;padding:0;box-sizing:border-box}
html,body{width:1200px;height:1200px;overflow:hidden;background:var(--bg)}
body{font-family:"Roboto",sans-serif;color:var(--ink)}
.stage{position:absolute;left:0;top:0;width:1500px;height:1500px;transform:scale(.8);transform-origin:0 0}
.sheet{position:absolute;left:325px;width:830px;height:640px;background:var(--paper);overflow:hidden}
.sheet--outside{top:82px}
.sheet--inside{top:765px}
.abs{position:absolute}
.footer{position:absolute;left:0;bottom:0;width:830px;height:26px;background:linear-gradient(90deg,var(--teal-light),#37b5d6);display:flex}
.footer span{flex:1;text-align:center;color:var(--white);font-family:"Poppins",sans-serif;font-size:19px;line-height:26px;font-weight:400}
.footer b{font-weight:700}
.h-display{font-family:"Poppins",sans-serif;font-weight:800;line-height:.95;letter-spacing:-.3px}
.small{font-size:9.8px;line-height:1.27}

/* outside: about panel */
.panel-about{left:0;top:0;width:275px;height:614px;background:linear-gradient(180deg,var(--teal) 0%,var(--blue) 100%);color:var(--white)}
.about-title{left:34px;top:32px;font-family:"Poppins",sans-serif;font-size:23px;line-height:.95;display:flex;align-items:flex-end;gap:4px;border-bottom:2px solid rgba(255,255,255,.8);padding-bottom:3px;white-space:nowrap}
.about-title .word{font-weight:300;display:block}
.about-title strong{font-weight:800;display:block}
.about-title .q{font-size:54px;font-weight:900;line-height:.8}
.about-copy{left:36px;top:89px;width:205px}
.about-copy p+p{margin-top:13px}
.pen-block{left:36px;top:283px;width:205px}
.pen-title{font-size:24px;white-space:nowrap}
.pen-title span{font-weight:400}
.pen-desc{font-size:9px;line-height:1.25;margin-top:12px}
.pen-list{list-style:none;font-size:9px;line-height:1.25}
.pen-list li::before{content:"•  "}
.chart-label{position:absolute;font-size:7px;line-height:1.05;color:var(--white);white-space:nowrap}

/* outside: hero + onset */
.hero{left:275px;top:0;width:278px;height:200px;background:radial-gradient(circle at 40% 45%,#6fd6dc 0%,#2fb8c8 45%,#1a93c9 100%)}
.hero-text{position:absolute;left:0;right:0;top:58px;text-align:center;color:var(--white);font-family:"Poppins",sans-serif;font-size:29px;line-height:.93}
.hero-text b{font-weight:800;display:block}
.onset{left:553px;top:0;width:277px;height:200px;background:linear-gradient(180deg,var(--teal) 0%,var(--blue) 100%);padding:44px 0 0 30px}
.onset-kicker{font-family:"Poppins",sans-serif;font-weight:700;font-size:16px;line-height:.9;color:var(--navy)}
.onset-big{font-family:"Poppins",sans-serif;font-weight:800;font-size:28px;color:var(--white);line-height:1.1}
.pills{display:grid;grid-template-columns:110px 110px;gap:5px 12px;margin-top:10px;margin-left:-5px}
.pill{height:15px;border-radius:8px;font-size:11px;font-weight:500;color:var(--navy);padding-left:6px;line-height:15px}
.pill::before{content:"• ";color:var(--white)}
.pill--a{background:#3fd0d6}.pill--b{background:#8fa4b8}

/* outside: patient support */
.support{left:275px;top:200px;width:278px;height:414px;background:var(--paper);text-align:center;color:#444}
.support > *{position:absolute;left:22px;right:22px}
.support h2{top:18px;font-family:"Poppins",sans-serif;font-weight:800;font-size:25px;line-height:1.2;color:var(--blue-deep);letter-spacing:-.2px}
.support-copy{top:53px;font-size:10px;line-height:1.27}
.offer{top:172px;border-top:1px solid #e4e4e4;padding-top:12px}
.offer h3{font-family:"Poppins",sans-serif;font-weight:800;font-size:13px;line-height:1.1;color:var(--blue-deep)}
.offer ul{list-style:none;font-size:13px;line-height:1.18;margin-top:5px}
.offer li::before{content:"•  ";color:var(--blue)}
.alliance{top:296px;border-top:1px solid #e4e4e4;padding-top:18px;display:flex;align-items:center;justify-content:center;gap:8px;font-family:"Poppins",sans-serif;font-weight:600;font-size:17px;line-height:1.2;color:var(--navy)}
.alliance i{width:10px;height:10px;border-radius:50%;background:var(--navy);display:block}
.contact{top:364px;font-size:10px;line-height:1.25}

/* outside: side panel */
.side{left:553px;top:200px;width:277px;height:414px;background:var(--paper-grey);border-top:4px solid #1b5e80}
.side-copy{position:absolute;left:28px;right:28px;top:178px;text-align:center;font-family:"Poppins",sans-serif;font-weight:600;font-size:12.5px;line-height:1.2;color:#333}
.gene-badge{display:inline-block;margin:6px 0 6px;background:var(--teal);color:var(--navy);font-weight:800;font-size:29px;padding:0 16px;border-radius:20px;line-height:34px}
.side-copy small{display:block;font-size:10.5px;line-height:1.2;margin:0 -8px}
.org-name{position:absolute;left:0;right:0;top:332px;text-align:center;font-family:"Poppins",sans-serif;font-weight:600;font-size:20px;color:var(--blue)}

/* inside */
.symptoms{left:0;top:0;width:275px;height:614px;background:#fbfbfb;padding:30px 20px 0}
.symptoms h2{font-family:"Poppins",sans-serif;font-weight:800;font-size:24px;line-height:1.2;color:var(--blue);border-bottom:2px solid var(--blue);display:inline-block;padding-right:8px}
.lead{font-family:"Poppins",sans-serif;font-weight:700;font-size:10px;line-height:1.28;color:var(--blue);margin-top:10px}
.cond{display:flex;gap:10px;margin-top:14px}
.num{flex:none;width:22px;height:22px;background:var(--blue-deep);color:var(--white);font-family:"Poppins",sans-serif;font-weight:700;font-size:13px;text-align:center;line-height:22px}
.cond h3{font-family:"Poppins",sans-serif;font-weight:800;font-size:14px;line-height:.95;color:var(--blue)}
.cond p{font-size:9.2px;line-height:1.23;margin-top:5px;color:#333}
.diag{left:275px;top:0;width:555px;height:328px;background:linear-gradient(135deg,var(--teal) 0%,var(--blue-deep) 100%);color:var(--white)}
.diag h2,.treat h2{font-family:"Poppins",sans-serif;font-weight:800;font-size:25px;line-height:1.2;color:var(--white);border-bottom:2px solid rgba(255,255,255,.7);display:inline-block;padding-right:10px}
.protein{left:20px;top:72px;width:243px;height:234px;background:radial-gradient(circle at 45% 55%,#1b6fd6 0%,#0d3a8a 35%,#05070f 75%)}
.diag-copy{position:absolute;left:292px;top:28px;width:250px;font-size:10.4px;line-height:1.24}
.diag-copy ul{list-style:none;margin-top:1px}
.diag-copy li{padding-left:14px;position:relative;font-weight:500}
.diag-copy li::before{content:"•";position:absolute;left:2px}
.treat{position:absolute;left:290px;top:178px;width:250px;font-size:10.4px;line-height:1.24}
.treat p{margin-top:12px;padding-left:2px}
.strength{left:297px;top:342px;font-family:"Poppins",sans-serif;font-weight:800;font-size:24px;line-height:.95;color:var(--teal)}
.research{left:299px;top:396px;font-family:"Poppins",sans-serif;font-weight:800;font-size:24px;line-height:1.05;color:var(--blue-deep);border-bottom:2px solid var(--blue-deep);padding-right:6px}
.res-left{position:absolute;left:299px;top:430px;width:230px;font-size:10.4px;line-height:1.24;color:#555}
.res-left .hl{color:var(--blue);font-size:11.5px;margin-top:6px}
.res-left .go{color:#333;font-size:12px;margin-top:14px}
.url-pill{display:inline-block;background:var(--blue-deep);color:var(--white);font-family:"Poppins",sans-serif;font-size:18px;padding:2px 12px;border-radius:16px;margin-top:4px;margin-left:-4px}
.url-pill b{font-weight:700}
.res-right{position:absolute;left:560px;top:430px;width:230px;font-size:10.4px;line-height:1.24;color:#555}
.registry{left:553px;top:546px;width:267px;height:40px;background:linear-gradient(90deg,#f3f6fa,#c9dcee)}
</style>
</head>
<body>
<div class="stage">

  <section class="sheet sheet--outside">
    <div class="abs panel-about">
      <h2 class="abs about-title"><span><span class="word">WHAT IS</span><strong>IBMPFD</strong></span><span class="q">?</span></h2>
      <div class="abs about-copy">
        <p class="small">Inclusion Body Myopathy associated with Paget's disease of bone &amp; Frontotemporal Dementia is an autosomal dominant mutation in chromosome 9 of the VCP (Valosin Containing Protein) gene. Given the interaction with other genetic diseases, this mutation may also be known as VCP Disease or Disorder.</p>
        <p class="small">Some patients have familial Amyotrophic Lateral Sclerosis (ALS or Lou Gehrig's disease) or Parkinson's which has been shown to have a pathogenic variant in VCP.</p>
      </div>
      <div class="abs pen-block">
        <h2 class="h-display pen-title">PENETRANCE <span>BY</span><br>PHENOTYPE</h2>
        <p class="pen-desc">The frequency that IBMPFD or VCP Disease manifests itself in one, two, or three primary disorders.</p>
        <ul class="pen-list">
          <li>IBM: Inclusion Body Myopathy</li>
          <li>PDB: Paget's Disease of the Bone</li>
          <li>FTD: Frontotemporal Dementia</li>
        </ul>
      </div>
      <svg class="abs" style="left:70px;top:452px" width="140" height="140" viewBox="0 0 140 140" aria-label="Donut chart of penetrance by phenotype">
        <g transform="rotate(-90 70 70)" fill="none" stroke-width="26">
          <circle cx="70" cy="70" r="50" stroke="#9fb3c6" stroke-dasharray="37 277" stroke-dashoffset="-43" pathLength="314"/>
          <circle cx="70" cy="70" r="50" stroke="#1f4fa8" stroke-dasharray="116 198" stroke-dashoffset="-80" pathLength="314"/>
          <circle cx="70" cy="70" r="50" stroke="#164b86" stroke-dasharray="85 229" stroke-dashoffset="-196" pathLength="314"/>
          <circle cx="70" cy="70" r="50" stroke="#6b8096" stroke-dasharray="16 298" stroke-dashoffset="-281" pathLength="314"/>
          <circle cx="70" cy="70" r="50" stroke="#c7cfd6" stroke-dasharray="10 304" stroke-dashoffset="-297" pathLength="314"/>
          <circle cx="70" cy="70" r="50" stroke="#5d6e7f" stroke-dasharray="6 308" stroke-dashoffset="-307" pathLength="314"/>
          <circle cx="70" cy="70" r="50" stroke="#dfe5ea" stroke-dasharray="31 283" stroke-dashoffset="-12" pathLength="314"/>
        </g>
      </svg>
      <span class="chart-label" style="left:80px;top:440px">PDB<br>only-5%</span>
      <span class="chart-label" style="left:120px;top:434px">FTD<br>only-3%</span>
      <span class="chart-label" style="left:164px;top:438px">IBM PDB<br>&amp; FTD-10%</span>
      <span class="chart-label" style="left:58px;top:460px">IBM &amp;<br>FTD -1%</span>
      <span class="chart-label" style="left:28px;top:510px">IBM &amp;<br>PDB -27%</span>
      <span class="chart-label" style="left:205px;top:505px">IBM<br>&amp; FTD<br>-1%</span>
      <span class="chart-label" style="left:114px;top:586px">IBM only- 37%</span>
    </div>

    <div class="abs hero" role="img" aria-label="Photo of many hands joined together in a circle, tinted teal">
      <div class="hero-text"><b>TOGETHER<br>WE CAN</b>MAKE A<br>DIFFERENCE</div>
    </div>

    <div class="abs onset">
      <p class="onset-kicker">DO YOU HAVE A FAMILY<br>HISTORY OF</p>
      <p class="onset-big">ADULT ONSET</p>
      <div class="pills">
        <span class="pill pill--a">Muscle Weakness?</span><span class="pill pill--b">Dementia?</span>
        <span class="pill pill--b">Bone Disease?</span><span class="pill pill--a">ALS?</span>
        <span class="pill pill--a">Parkinson's?</span><span class="pill pill--b">IBM?</span>
      </div>
    </div>

    <div class="abs support">
      <h2>PATIENT SUPPORT</h2>
      <p class="support-copy">Mend ORX Syndrome, Inc. is a 501(c)(3) which was formed to drive efforts to cure diseases related to mutations of the Valosin Containing Protein (VCP) gene. <b>Our main goal is to bring patients and doctors together</b> so we can help one another and drive research towards a cure.<br><b>We are also trying to bring awareness to the medical community about our rare disease.</b></p>
      <div class="offer">
        <h3>WE OFFER RESOURCES &amp;<br>SUPPORT TO PATIENTS,<br>CAREGIVERS AND DOCTORS.<br>CONNECT WITH US.</h3>
        <ul>
          <li>IBMPFD social media page</li>
          <li>MendORX.org</li>
          <li>IBMPFD-info.net</li>
        </ul>
      </div>
      <div class="alliance"><i></i>RAREWELL ALLIANCE</div>
      <p class="contact"><b>Mend ORX Syndrome, Inc.</b><br>P.O. Box 4120 | Lakeview, OR 97630<br>hello@mendorx.org</p>
    </div>

    <div class="abs side">
      <svg class="abs" style="left:48px;top:-16px" width="188" height="188" viewBox="0 0 188 188" aria-hidden="true">
        <circle cx="94" cy="94" r="90" fill="none" stroke="var(--blue)" stroke-width="4"/>
      </svg>
      <div class="abs" role="img" aria-label="Photo of a smiling doctor with a stethoscope talking with a patient" style="left:54px;top:-10px;width:176px;height:176px;border-radius:50%;background:radial-gradient(circle at 45% 40%,#f1e3d6 0%,#d9d4cf 45%,#eef2f5 100%)"></div>
      <div class="side-copy">
        You may consider talking to your doctor about a mutation of the VCP gene called<br>
        <span class="gene-badge">IBMPFD</span>
        <small>Inclusion Body Myopathy associated with Paget's Disease of Bone and Frontotemporal Dementia</small>
      </div>
      <p class="org-name">Mend ORX Syndrome</p>
    </div>

    <div class="footer"><span>www.<b>mendorx</b>.org</span><span>www.<b>mendorx</b>.org</span><span>www.<b>mendorx</b>.org</span></div>
  </section>

  <section class="sheet sheet--inside">
    <div class="abs symptoms">
      <h2>SYMPTOMS:</h2>
      <p class="lead">IMBPFD, A VCP DISEASE, IS AN ~ADULT ONSET DISORDER THAT CAN AFFECT THE MUSCLES, BONES, AND BRAIN, AND AN AFFECTED PATIENT MAY HAVE ANY COMBINATION OF THE FOLLOWING CONDITIONS:</p>
      <div class="cond"><span class="num">1</span><div><h3>INCLUSION BODY<br>MYOPATHY:</h3>
        <p>The first symptom of IBMPFD is often muscle weakness (myopathy). Typically, patients first notice difficulty raising arms, losing balance or difficulty climbing stairs. As the disorder progresses, weakness develops in the other muscles in the arms, legs and core muscles. Muscle weakness can also affect respiratory and heart (cardiac) muscles. This disorder may first present in an individual's late 30's and over time occurs in approximately 90% of individuals with VCP Disease.</p></div></div>
      <div class="cond"><span class="num">2</span><div><h3>PAGET'S DISEASE OF BONE:</h3>
        <p>Bone pain, particularly in the hips and spine, is usually the major symptom of Paget's disease. It most often affects bones of the hips, spine, and skull, and the long bones of the arms and legs. Paget's disease affects half of individuals with VCP Disease and typically first presents in a person's 30's or 40's, which is a much earlier age than those without VCP Disease.</p></div></div>
      <div class="cond"><span class="num">3</span><div><h3>FRONTOTEMPORAL<br>DEMENTIA:</h3>
        <p>In about one-third of people with VCP Disease, the disorder also affects the brain. FTD typically changes personality, behavior, language and speech. FTD typically presents in the mid-50's. Amyotrophic Lateral Sclerosis (ALS or Lou Gehrig's disease): ALS occurs in approximately 10% of individuals with VCP Disease. Symptoms include increased muscle tone, weakness, muscle wasting, muscle cramps, difficulty swallowing and speaking.</p></div></div>
    </div>

    <div class="abs diag">
      <h2 class="abs" style="left:22px;top:22px">DIAGNOSIS:</h2>
      <div class="abs protein" role="img" aria-label="Ribbon diagram of the VCP protein structure with N-domain, linker and D1 ATPase domain"></div>
      <div class="diag-copy">
        <p>The only way of diagnosing VCP Disease is through genetic testing. Consult with your doctor about testing for mutations of the VCP gene.</p>
        <p style="margin-top:9px">For information about genetic testing, our two medical advisors are available as resources:</p>
        <ul>
          <li>Dr. Helena Marsh, Medical Geneticist at Northfield Medical University, hmarsh@northfield.edu</li>
          <li style="margin-top:5px">Dr. Peter Lindqvist, Neuromuscular Specialist at Eastbrook University,</li>
        </ul>
      </div>
      <div class="treat">
        <h2>TREATMENT</h2>
        <p>There is an approved treatment for Paget's disease of bone, so early testing for this disorder is very important.<br>There are no known cures or treatments for the Inclusion Body Myopathy or Frontotemporal Dementia. Consult with your doctor about physical therapy, stretching, diet and mobility aids.</p>
      </div>
    </div>

    <p class="abs strength">STRENGTH THROUGH NUMBERS<br>WILL HELP US FIND A CURE!</p>
    <h2 class="abs research">RESEARCH:</h2>
    <div class="res-left">
      <p>The goal of the RDPR registry is to connect as many patients and researchers as possible to help advance treatments &amp; cures for rare diseases.</p>
      <p class="hl">If you have been diagnosed with IBMPFD or VCP Disease, please help us by completing the patient registry through RDPR.</p>
      <p class="go">Go to our website</p>
      <span class="url-pill">www.<b>mendorx</b>.org</span>
      <p style="color:#333;font-size:12px;margin-top:6px">to access the RDPR Registry.</p>
    </div>
    <div class="res-right">
      <p>The RDPR registry is free for patients to enroll and for researchers to access.</p>
      <p style="margin-top:14px">Please elect for researchers to have access to your registry, as that will greatly assist in the drive for a cure, especially when drug trials are recruiting patients</p>
    </div>
    <div class="abs registry" role="img" aria-label="Registry partner badge"></div>

    <div class="footer"><span>www.<b>mendorx</b>.org</span><span>www.<b>mendorx</b>.org</span><span>www.<b>mendorx</b>.org</span></div>
  </section>

</div>
</body>
</html>
```